Halvorn Analytics, Inc. Site Design Project

Halvorn Analytics, Inc is my private and small research office.
This naming shows:
We investigate every(*: asterisk) issue to support society.
We investigate "a star risk" which means every critical things for example, information security, branding, public communication - to understand for our clients - especially innovative person.
Last year, we had faced the great disaster in Japan, we investigated the damaged place, schools, and local governments, and supported communities like PLUMvaskel.
So I want to get a high concept sites with good logo and to use card, website, and our letter.
Reason: We would like to look for more competitive candidates.
I uploaded the latest logo. If you have any idea to adapt it to your design, I appreciate it.
Target Market(s)
* marketing section of leading companies(enterprises)
* promotion agencies of government
* futurist and researcher
* business managers
Industry/Entity Type
Communication
Logo Text
for desirable future
Look and feel
Each slider illustrates characteristics of the customer's brand and the style your logo design should communicate.

```html
<!DOCTYPE html>
<html lang="en">
<head>
<meta charset="utf-8">
<title>Halvorn Analytics, Inc</title>
<link href="https://fonts.googleapis.com/css2?family=Arimo:wght@400;700&family=Roboto+Condensed:wght@400;700&family=Tinos:ital,wght@0,400;0,700;1,400;1,700&display=swap" rel="stylesheet">
<style>
:root{
  --red:#d70000;
  --ink:#111;
  --page:#efefef;
  --panel:#fff;
  --rule:#222;
  --foot:#050505;
  --foot-grey:#5a5a5a;
  --muted:#999;
  --serif:'Tinos', serif;
  --sans:'Arimo', sans-serif;
  --cond:'Roboto Condensed', sans-serif;
}
*{box-sizing:border-box;margin:0;padding:0}
html,body{width:1114px;height:1200px;overflow:hidden}
body{position:relative;background:var(--page);font-family:var(--sans);color:var(--ink)}
.abs{position:absolute}

.brand{left:133px;top:24px;display:flex;align-items:center;gap:10px}
.brand-mark{width:30px;height:30px;background:var(--red)}
.brand-name{font-family:var(--cond);font-size:27px;line-height:29px;letter-spacing:5px;color:#222;font-weight:400}
.phone{right:134px;top:26px;display:flex;align-items:center;gap:4px;font-family:var(--cond);font-weight:700;font-size:28px;color:#111}

.panel{left:115px;top:104px;width:884px;height:829px;background:var(--panel);border-left:1px solid #888;border-right:1px solid #888;border-top:4px solid var(--red)}
.nav{left:457px;top:65px;width:542px;height:43px;background:var(--red);clip-path:polygon(36px 0,100% 0,100% 100%,0 100%)}
.nav-edge{left:457px;top:65px;width:42px;height:43px;background:#000;clip-path:polygon(36px 0,42px 0,6px 100%,0 100%)}
.nav ul{list-style:none;display:flex;justify-content:space-between;padding:16px 18px 0 47px;font-family:var(--serif);font-weight:700;font-size:15.5px;color:#fff}

.hero{left:133px;top:126px;width:848px;height:309px;background:linear-gradient(100deg,#2f8fd0 0%,#7cc2ea 35%,#cfe6ef 55%,#e9c2a6 75%,#d9a184 100%)}
.hero h1{position:absolute;left:44px;top:70px;font-family:var(--cond);font-weight:700;font-size:31px;line-height:39px;color:#fff;letter-spacing:-.3px}
.btn{position:absolute;background:var(--red);color:#fff;font-family:var(--serif);font-weight:700}
.hero .btn{left:46px;top:154px;width:128px;height:27px;font-size:14px;text-align:center;line-height:27px}
.dots{position:absolute;right:8px;bottom:5px;display:flex;gap:3px}
.dots i{width:7px;height:7px;border-radius:50%;background:#fff}
.dots i:first-child{background:#000}

.card{top:453px;width:221px;height:151px}
.card .shot{height:115px}
.card .label{height:36px;background:#000;color:#fff;font-family:var(--cond);font-weight:700;font-size:14.5px;line-height:36px;padding-left:37px;position:relative}
.card .label::before{content:"";position:absolute;left:0;top:0;width:36px;height:36px;background:linear-gradient(135deg,transparent 0 45%,var(--red) 45% 62%,transparent 62%)}

.find{left:831px;top:453px;width:150px;height:151px;background:repeating-linear-gradient(135deg,#fde4e4 0 3px,#fff 3px 6px);padding:12px 18px}
.find h3{font-family:var(--serif);font-weight:700;font-size:15.5px;color:var(--red);border-bottom:3px solid var(--red);padding-bottom:1px;margin-bottom:10px}
.find li{list-style:none;display:flex;align-items:center;gap:7px;font-size:13.5px;height:24.5px}
.sq{width:18px;height:18px;display:inline-block;border-radius:2px}
.c1{background:#3b5b9a}.c2{background:#3fc1e6}.c3{background:#1f7db8}.c4{background:#c8271e}

.welcome{left:133px;top:633px;width:604px}
.welcome h2{font-family:var(--serif);font-weight:700;font-size:22.5px;color:var(--red);border-bottom:2px solid var(--red);padding-bottom:0;margin-bottom:16px}
.welcome p{font-size:11px;line-height:14.2px;margin-bottom:10.5px}
.welcome a{color:var(--red);font-weight:700;text-decoration:none}
.divider{left:760px;top:630px;width:1px;height:276px;background:var(--rule)}

.recent{left:782px;top:639px;width:199px}
.recent h3{height:27px;font-family:var(--serif);font-weight:700;font-size:16px;line-height:27px;padding-left:5px;background:repeating-linear-gradient(135deg,#ddd 0 2px,#f4f4f4 2px 5px)}
.recent li{list-style:none;height:29px;line-height:29px;padding-left:7px;color:var(--red);font-family:var(--cond);font-size:11.5px;border-bottom:1px solid var(--rule)}
.recent li:last-child{border-bottom:none}

.footer{left:0;top:933px;width:1114px;height:267px;background:var(--foot);border-top:3px solid var(--red)}
.fcol{top:968px;width:253px;color:#fff}
.fcol h4{font-family:var(--cond);font-weight:400;font-size:16.5px;color:#ccc;border-bottom:3px solid #777;padding-bottom:1px;margin-bottom:19px}
.map{height:106px;background:linear-gradient(135deg,#e9e4d6,#f3efe6 60%,#d8e6cf)}
.addr{font-family:var(--serif);font-weight:700;font-size:11px;line-height:15px;margin-top:8px}
.quote{background:var(--foot-grey);height:140px;padding:15px 14px;font-family:var(--serif);font-style:italic;font-weight:700;font-size:11px;line-height:17px;color:#f2f2f2;position:relative}
.quote cite{display:block;text-align:right;font-size:9.5px;line-height:11px;margin-top:9px}
.quote::after{content:"";position:absolute;right:17px;bottom:-18px;border-left:10px solid transparent;border-top:18px solid var(--foot-grey)}
.email{height:31px;background:var(--foot-grey);border-radius:3px;padding-left:10px;font-family:var(--serif);font-style:italic;font-size:11px;line-height:31px;color:#aaa}
.fcol .btn{position:static;display:block;margin:8px 0 0 auto;width:114px;height:26px;text-align:center;line-height:26px;font-size:14px}
.also{text-align:right;margin-top:12px;font-family:var(--cond);font-weight:700;font-size:11px;padding-right:20px}
.also-icons{display:flex;justify-content:flex-end;gap:10px;margin-top:6px}
.copy{right:133px;top:1180px;font-family:var(--serif);font-weight:700;font-size:8.5px;color:#888}
</style>
</head>
<body>

<div class="abs panel"></div>

<div class="abs brand">
  <span class="brand-mark"></span>
  <span class="brand-name">HALVORN<br>ANALYTICS</span>
</div>

<div class="abs phone">
  <svg width="24" height="24" viewBox="0 0 24 24" aria-hidden="true"><rect x="2" y="3" width="10" height="19" rx="1.5" fill="#111"/><rect x="4" y="5" width="6" height="5" fill="#fff"/><path d="M15 6a6 6 0 0 1 0 8M18 3a10 10 0 0 1 0 14" stroke="#111" stroke-width="2" fill="none"/></svg>
  03.5550.4182
</div>

<div class="abs nav-edge"></div>
<nav class="abs nav">
  <ul><li>*About</li><li>*Services</li><li>*Projects</li><li>*Press Releases</li><li>*Contact</li></ul>
</nav>

<section class="abs hero" role="img" aria-label="Close-up photo of a woman in glasses looking at a blue screen">
  <h1>LATEST REPORT FROM<br>HALVORN ANALYTICS, INC</h1>
  <span class="btn">*Learn&nbsp; More</span>
  <div class="dots"><i></i><i></i><i></i><i></i></div>
</section>

<article class="abs card" style="left:133px">
  <div class="shot" role="img" aria-label="Photo of houses destroyed by a disaster" style="background:linear-gradient(180deg,#c9cdd2,#8a7d6e 60%,#5a5148)"></div>
  <div class="label">NATURAL DISASTER REPORT</div>
</article>
<article class="abs card" style="left:362px">
  <div class="shot" role="img" aria-label="Photo of a login screen with username and password fields" style="background:linear-gradient(135deg,#0a2a66,#1e5fb8 50%,#06183f)"></div>
  <div class="label">INFO. SECURITY REPORT</div>
</article>
<article class="abs card" style="left:592px">
  <div class="shot" role="img" aria-label="Photo of a businessman speaking to press microphones" style="background:linear-gradient(135deg,#3c4656,#b89a84 45%,#6e7888)"></div>
  <div class="label">PUBLIC COMM. REPORT</div>
</article>

<aside class="abs find">
  <h3>*Find Us On</h3>
  <ul>
    <li><span class="sq c1"></span>Friendwall</li>
    <li><span class="sq c2"></span>Chirpline</li>
    <li><span class="sq c3"></span>Workweb</li>
    <li><span class="sq c4"></span>Clipstream</li>
  </ul>
</aside>

<section class="abs welcome">
  <h2>*Welcome to Halvorn Analytics, Inc</h2>
  <p>Lorem ipsum dolor sit amet, consectetur adipiscing elit. Praesent fermentum lacus non leo vestibulum venenatis. Nam at sodales dolor. Maecenas condimentum dictum odio non iaculis. Aenean neque diam, porta auctor euismod eu, viverra quis nisi. Sed dapibus nisl sit amet risus auctor in tempor diam rhoncus. Donec quis nisi leo. Morbi dignissim congue ligula, id porttitor nulla. Donec a elit sem. Pellentesque et nulla ut quam auctor aliquet. Etiam at ipsum eu erat fermentum.</p>
  <p>Mauris laoreet sem quis nulla eleifend auctor malesuada dolor pellentesque. Cras accumsan rutrum magna. Class aptent taciti sociosqu ad litora torquent per conubia nostra, per inceptos himenaeos. Vestibulum elementum, neque vitae convallis faucibus, elit leo vulputate sapien, vel imperdiet felis lorem a enim. Nulla facilisi. Phasellus vel urna at diam consectetur laoreet pulvinar at quam. Sed mauris felis, congue quis dignissim sed, rutrum a justo vivamus est neque.</p>
  <p>Ut ut sem nec leo hendrerit scelerisque luctus ac nunc. Pellentesque dignissim vestibulum vestibulum. Ut luctus velit vitae neque rhoncus vel blandit neque placerat. Phasellus vestibulum leo accumsan lorem tempor posuere. Vivamus mi ligula, fringilla id ullamcorper id, suscipit quis mauris. Praesent rhoncus neque et metus ornare porttitor. Vestibulum ante ipsum primis in faucibus orci luctus et ultrices posuere cubilia Curae; Vestibulum nunc lacus, consequat tincidunt eleifend eget, adipiscing sit amet purus. Mauris nec risus nisi. Cras vehicula dui a eros convallis faucibus. Proin quis nisi eu lacus porta volutpat ullamcorper a urna. Phasellus erat sem, eleifend in egestas in, aliquam a nibh <a href="#">contact us</a>.</p>
</section>

<div class="abs divider"></div>

<aside class="abs recent">
  <h3>*Recent Projects</h3>
  <ul>
    <li>LOREM IPSUM DOLOR SIT AMET</li>
    <li>CONSECTETUR ADIPISCING</li>
    <li>PRAESENT FERMENTUM</li>
    <li>LACUS NON LEO VESTIBULUM</li>
    <li>VENENATIS</li>
  </ul>
</aside>

<footer class="abs footer"></footer>

<div class="abs fcol" style="left:133px">
  <h4>HALVORN ANALYTICS, INC</h4>
  <div class="map" role="img" aria-label="Street map showing the office location"></div>
  <p class="addr">7-4 Minato Koto-ku Tokyo 135-0044 Japan<br>03.5550.4182<br>hello@halvornanalytics.jp</p>
</div>

<div class="abs fcol" style="left:430px">
  <h4>TESTIMONIAL</h4>
  <blockquote class="quote">
    Lorem ipsum dolor sit amet, consectetur adipiscing elit. Praesent fermentum lacus non leo vestibulum venenatis. Nam at sodales dolor. Maecenas condimentum dictum odio non iaculis. Aenean neque diam, porta auctori.
    <cite>Marcus, Editorial Manager<br>Northgate Media</cite>
  </blockquote>
</div>

<div class="abs fcol" style="left:728px">
  <h4>CONNECT WITH US</h4>
  <div class="email">Enter your email to recieve our newsletter</div>
  <span class="btn">*Sign Me Up</span>
  <p class="also">ALSO FIND US ON:</p>
  <div class="also-icons"><span class="sq c1"></span><span class="sq c2"></span><span class="sq c3"></span><span class="sq c4"></span></div>
</div>

<p class="abs copy">©2012 Halvorn Analytics, Inc.</p>

</body>
</html>
```